Design and Renovation Company Luxury Business Card

I want to create a luxury business card for a Design and Renovation Firm . We will use our current logo. The company name is 742BUILD. We do not want anything standard. We need a very unique concept.
Please see uploaded inspiration. I really like the textured paper option. I would like the card to be thick with debossing, and/or embossing options. The logo has orange in it but I would like to see the card with and without the orange. I think the orange may make the company feel less high-end. The goal is to elevate the logo not match its vibe per se of the logo. We want something very unique, not standard at all!
I would like a space for :
Logo,
Name,
Position,
Email,
Office number,
Website Address,
Business Address,
Thank you!
Have fun!
Target Market(s)
Home owners Age 35 +
Industry/Entity Type
Design and Renovation
Contact Information for Business Card
Logo, Name, Position, Email, Office number, Website Address, Business Address,.
Colors
Designer to choose colors to be used in the design.
Requirements
Must have
- A luxury designer feel. Must be black or dark grey but open to other luxury ideas.
Nice to have
- Gold, silver, black embossing or debossing. Textured paper design.
Should not have
- A cheap look and feel.

```html
<!DOCTYPE html>
<html lang="en">
<head>
<meta charset="utf-8">
<title>742BUILD Business Card</title>
<link rel="stylesheet" href="https://fonts.googleapis.com/css2?family=Poppins:wght@400;500;600&display=swap">
<style>
  :root {
    --page: #f6f6f6;
    --card: #000000;
    --gold: #fde08e;
    --shadow: rgba(0, 0, 0, 0.35);
  }
  * { margin: 0; padding: 0; box-sizing: border-box; }
  html, body { width: 1200px; height: 2410px; overflow: hidden; }
  body {
    background: var(--page);
    font-family: "Poppins", sans-serif;
    color: var(--gold);
    position: relative;
  }
  .card {
    position: absolute;
    left: 75px;
    width: 1050px;
    background: var(--card);
    box-shadow: 0 2px 8px var(--shadow);
    overflow: hidden;
  }
  .card-front { top: 590px; height: 580px; }
  .card-back { top: 1222px; height: 605px; }

  /* Company name */
  .company {
    display: flex;
    align-items: center;
    gap: 16px;
  }
  .company-dot {
    border-radius: 50%;
    background: var(--gold);
    flex: none;
  }
  .company-name {
    font-weight: 400;
    line-height: 1;
  }

  /* Front */
  .front-company {
    position: absolute;
    top: 180px;
    left: 0; right: 0;
    justify-content: center;
  }
  .front-company .company-dot { width: 22px; height: 22px; }
  .front-company .company-name { font-size: 64px; letter-spacing: 5px; }

  .front-message {
    position: absolute;
    top: 336px;
    left: 0; right: 0;
    text-align: center;
  }
  .thanks { font-size: 48px; font-weight: 400; line-height: 1.1; }
  .have-fun { font-size: 26px; font-weight: 400; letter-spacing: 4px; margin-top: 2px; }

  /* Back */
  .back-lines { position: absolute; inset: 0; }
  .back-company {
    position: absolute;
    left: 74px;
    top: 294px;
    gap: 11px;
  }
  .back-company .company-dot { width: 14px; height: 14px; }
  .back-company .company-name { font-size: 40px; letter-spacing: 3px; }

  .divider {
    position: absolute;
    left: 468px;
    top: 239px;
    width: 3px;
    height: 196px;
    background: var(--gold);
  }
  .person {
    position: absolute;
    right: 53px;
    top: 110px;
    text-align: center;
  }
  .person-name { font-size: 72px; font-weight: 600; line-height: 1; letter-spacing: 1px; }
  .person-role { font-size: 20px; font-weight: 500; margin-top: 4px; }

  .contact {
    position: absolute;
    right: 53px;
    top: 232px;
    list-style: none;
    text-align: right;
    font-size: 21.5px;
    font-weight: 500;
    line-height: 27px;
  }
  .contact li { display: flex; justify-content: flex-end; align-items: center; gap: 16px; }
  .contact li + li { margin-top: 14px; }
  .contact .email, .contact .web { margin-top: 12px; }
  .contact .web span { letter-spacing: 2px; }
  .icon { width: 22px; height: 22px; flex: none; }
</style>
</head>
<body>

<section class="card card-front">
  <div class="company front-company">
    <span class="company-dot"></span>
    <span class="company-name">742BUILD</span>
  </div>
  <div class="front-message">
    <p class="thanks">THANK YOU!</p>
    <p class="have-fun">HAVE FUN!</p>
  </div>
</section>

<section class="card card-back">
  <svg class="back-lines" width="1050" height="605" viewBox="0 0 1050 605">
    <path d="M140 0 V92 A47 47 0 0 1 93 139 H0" fill="none" stroke="#fde08e" stroke-width="3"/>
    <path d="M0 453 H93 A47 47 0 0 1 140 500 V605" fill="none" stroke="#fde08e" stroke-width="3"/>
    <rect x="140" y="591" width="860" height="14" fill="#fde08e"/>
  </svg>

  <div class="company back-company">
    <span class="company-dot"></span>
    <span class="company-name">742BUILD</span>
  </div>

  <div class="divider"></div>

  <div class="person">
    <p class="person-name">ADAM REYES</p>
    <p class="person-role">DIRECTOR</p>
  </div>

  <ul class="contact">
    <li class="address"><span>18 HARBOUR CREST DRIVE OAKRIDGE,<br>ONTARIO CANADA L2K 4P8</span></li>
    <li class="phone">
      <span>18 HARBOUR CREST DRIVE OAKRIDGE,<br>ONTARIO CANADA L2K 4P8</span>
      <svg class="icon" viewBox="0 0 22 22"><circle cx="11" cy="11" r="10" fill="none" stroke="#fde08e" stroke-width="2"/><path d="M7.5 6.5 l2 0 1 2.5 -1.3 1 a6 6 0 0 0 2.8 2.8 l1 -1.3 2.5 1 0 2 a1.2 1.2 0 0 1 -1.2 1.2 A8 8 0 0 1 6.3 7.7 a1.2 1.2 0 0 1 1.2 -1.2z" fill="#fde08e"/></svg>
    </li>
    <li class="email">
      <span>INFO@742BUILD.COM</span>
      <svg class="icon" viewBox="0 0 22 22"><circle cx="11" cy="11" r="10" fill="none" stroke="#fde08e" stroke-width="2"/><rect x="6" y="7.5" width="10" height="7" fill="none" stroke="#fde08e" stroke-width="1.5"/><path d="M6 7.5 L11 11.5 L16 7.5" fill="none" stroke="#fde08e" stroke-width="1.5"/></svg>
    </li>
    <li class="web">
      <span>WWW.742BUILD.COM</span>
      <svg class="icon" viewBox="0 0 22 22"><circle cx="11" cy="11" r="10" fill="none" stroke="#fde08e" stroke-width="2"/><circle cx="11" cy="11" r="5.5" fill="none" stroke="#fde08e" stroke-width="1.4"/><ellipse cx="11" cy="11" rx="2.3" ry="5.5" fill="none" stroke="#fde08e" stroke-width="1.2"/><path d="M5.5 11 H16.5" stroke="#fde08e" stroke-width="1.2"/></svg>
    </li>
  </ul>
</section>

</body>
</html>
```